Aviation: IFR Study Guide Book Cover

We need a book cover (front and back) designed for an Instrument Flight Rules (IFR) study guide used by helicopter and airplane pilots to obtain an instrument rating for a helicopter or airplane. Below is the title and subtitles.

TITLE: IFR STUDY GUIDE
SUBTITLE 1: Checkride Preparation for Airplane and Helicopter Pilots
SUBTITLE 2: Prepare for your Instrument Rating with Confidence

We have also upload recommended text to be included on the back cover. In addition, we included images of similar book covers that we like and ones that we do not like. Below are links to two others books by the author.

https://www.shopvendrix.com/Rotorcraft-Exam-Handbook-oral-flighttest/dp/204715382K
https://www.shopvendrix.com/Manual-Floatcraft-Piloting-Marcus-Holloway/dp/1702538146

Target Market(s)

Flight students

Industry/Entity Type

Aviation

Requirements
Nice to have
• helicopter and airplane

```html
<!DOCTYPE html>
<html lang="en">
<head>
<meta charset="utf-8">
<title>IFR Study Guide – Cover Spread</title>
<link href="https://fonts.googleapis.com/css2?family=Poppins:ital,wght@0,400;0,500;0,600;0,700;0,800;0,900;1,500&display=swap" rel="stylesheet">
<style>
  :root {
    --page: #ffffff;
    --teal: #0d6e91;
    --mid-blue: #0b4f7c;
    --navy: #0a2552;
    --gold: #e8a92a;
    --white: #ffffff;
    --tag-bg: #0d3f78;
    --cockpit-light: #8ea3b8;
    --cockpit-dark: #2a3a52;
  }
  * { margin: 0; padding: 0; box-sizing: border-box; }
  html, body { width: 1200px; height: 900px; overflow: hidden; background: var(--page); }
  body { position: relative; font-family: "Poppins", sans-serif; color: var(--white); }

  .cover-spread {
    position: absolute; left: 70px; top: 104px; width: 1060px; height: 678px;
    background: linear-gradient(180deg, var(--teal) 0%, var(--mid-blue) 55%, var(--navy) 100%);
    overflow: hidden;
  }

  /* Back cover */
  .back-heading {
    position: absolute; left: 45px; width: 430px;
    font-size: 11.6px; font-weight: 600; color: var(--gold); letter-spacing: -0.1px;
  }
  .back-body {
    position: absolute; left: 45px; width: 429px;
    font-size: 10.2px; line-height: 12px; text-align: justify;
  }
  .topic-tags { position: absolute; left: 43px; top: 244px; width: 380px; }
  .topic-tag {
    position: absolute; width: 117px; height: 19px; background: var(--tag-bg);
    font-size: 9px; line-height: 19px; padding-left: 9px;
  }
  .author-heading {
    position: absolute; left: 45px; top: 322px;
    font-size: 21px; font-weight: 400; color: var(--gold);
  }
  .author-heading strong { font-weight: 800; }
  .author-bio {
    position: absolute; left: 45px; top: 358px; width: 429px;
    font-size: 10px; line-height: 14.4px; text-align: justify;
  }

  /* Spine */
  .spine-title, .spine-author {
    position: absolute; writing-mode: vertical-rl; font-weight: 900; white-space: nowrap;
  }
  .spine-title { left: 518px; top: 56px; font-size: 20px; letter-spacing: 1px; color: var(--white); }
  .spine-author { left: 522px; top: 412px; font-size: 13.5px; letter-spacing: 0.4px; color: var(--gold); }

  /* Front cover */
  .cockpit-photo { position: absolute; left: 543px; top: 340px; width: 517px; height: 338px; }
  .front-title { position: absolute; left: 574px; top: 18px; font-weight: 900; }
  .title-ifr { display: block; font-size: 142px; line-height: 142px; color: var(--gold); letter-spacing: -4px; }
  .title-study, .title-guide { display: block; font-size: 72px; line-height: 58px; color: var(--white); letter-spacing: -2px; }
  .title-study { margin-top: -8px; }
  .rule { position: absolute; height: 1.5px; background: var(--gold); }
  .rule.light { background: #d9dde6; }
  .front-subtitle { position: absolute; left: 583px; top: 272px; font-size: 15.5px; line-height: 20px; }
  .front-subtitle .line-1 { font-weight: 400; display: block; }
  .front-subtitle .line-2 { font-weight: 700; display: block; }
  .front-tagline {
    position: absolute; left: 578px; top: 556px; font-size: 17.5px; line-height: 21px;
    font-weight: 700; letter-spacing: 2.2px;
  }
  .front-tagline .gold { color: var(--gold); display: block; }
  .front-tagline .white { display: block; }
  .front-author {
    position: absolute; left: 578px; top: 618px; font-size: 27px; font-weight: 800;
    color: var(--gold); letter-spacing: 1.8px;
  }
  .instrument-stack { position: absolute; left: 932px; top: 26px; }
</style>
</head>
<body>
  <main class="cover-spread">
    <!-- Back cover -->
    <h2 class="back-heading" style="top:48px">PREPARE FOR YOUR IFR CHECK RIDE WITH CONFIDENCE</h2>
    <p class="back-body" style="top:68px">Becoming an instrument rated pilot is one of the most challenging ratings to obtain. This guide helps prepare you to pass your IFR check ride with confidence. The question-and-answer format is easy to follow and provides detailed explanations for expanded knowledge.</p>

    <h2 class="back-heading" style="top:126px">INCLUDES HELICOPTER AND AIRPLANE SPECIFIC CONTENT</h2>
    <p class="back-body" style="top:143px">This guide is designed to prepare an airplane or helicopter pilot the oral portion of the IFR checkride. Unlike other resources, this guide specifically addresses the differences with IFR flight in helicopters. As a dual rated pilot, the author ensures to identify areas of differences between the two categories of IFR flight. The following concepts are addressed within the guide.</p>

    <div class="topic-tags">
      <span class="topic-tag" style="left:0;top:0">Preflight Actions</span>
      <span class="topic-tag" style="left:127px;top:0">Enroute Procedures</span>
      <span class="topic-tag" style="left:254px;top:0">Aeromedical Factors</span>
      <span class="topic-tag" style="left:0;top:24px">General IFR Concepts</span>
      <span class="topic-tag" style="left:127px;top:24px">Approach Procedures</span>
      <span class="topic-tag" style="left:254px;top:24px">Weather Fundamentals</span>
      <span class="topic-tag" style="left:0;top:49px">Departure Procedures</span>
      <span class="topic-tag" style="left:127px;top:49px;padding-left:14px">IFR Emergence</span>
      <span class="topic-tag" style="left:254px;top:49px;padding-left:13px">Risk Management</span>
    </div>

    <h2 class="author-heading"><strong>About</strong> the Author</h2>
    <p class="author-bio">Marcus Holloway is ATP rated pilot and helicopter and fixed-wing instructor. Marcus is the owner and operator Northline Summit, LLC which does business as Vantage Rotor Aviation and Pelican Float Aviation. Vantage Rotor Aviation provides primary helicopter flight instruction while Pelican Float Aviation provides seaplane flight instruction and tours. In addition to instructing, Marcus has authored other books to include <em>The Rotorcraft Exam Handbook</em>, and <em>Manual of Floatcraft Piloting</em>. Marcus lives in Kentucky with his beautiful wife Dana. They have a daughter, Claire, that is dual rated and employed as a captain for a charter company. Prior to learning to fly, Marcus spent several years in the military as a Special Warfare Combat Craft Crewman in the U.S. Navy and Ranger-qualified Infantry Officer in the WV Army National Guard.</p>

    <!-- Spine -->
    <div class="spine-title">IFR STUDY GUIDE</div>
    <div class="spine-author">MARCUS J. HOLLOWAY</div>

    <!-- Front cover -->
    <svg class="cockpit-photo" viewBox="0 0 517 338" role="img" aria-label="Photograph of an airliner cockpit instrument panel and control yokes">
      <defs>
        <linearGradient id="cockpitTone" x1="0" y1="0" x2="0" y2="1">
          <stop offset="0" stop-color="var(--cockpit-light)" stop-opacity="0.85"/>
          <stop offset="0.5" stop-color="var(--cockpit-dark)" stop-opacity="0.9"/>
          <stop offset="1" stop-color="var(--navy)" stop-opacity="1"/>
        </linearGradient>
      </defs>
      <path d="M0 50 Q200 -5 517 20 L517 338 L0 338 Z" fill="url(#cockpitTone)"/>
    </svg>

    <h1 class="front-title">
      <span class="title-ifr">IFR</span>
      <span class="title-study">STUDY</span>
      <span class="title-guide">GUIDE</span>
    </h1>

    <div class="rule" style="left:583px;top:268px;width:268px"></div>
    <p class="front-subtitle">
      <span class="line-1">CHECKRIDE PREPARATION FOR</span>
      <span class="line-2">AIRPLANE &amp; HELICOPTER PILOTS</span>
    </p>
    <div class="rule" style="left:583px;top:314px;width:268px"></div>

    <svg class="instrument-stack" width="96" height="510" viewBox="0 0 96 510">
      <g stroke="var(--gold)" stroke-width="3">
        <circle cx="48" cy="47" r="45" fill="#1a1d22" role="img" aria-label="Airspeed indicator"/>
        <circle cx="48" cy="150" r="45" fill="#5a6f9a" role="img" aria-label="Attitude indicator"/>
        <circle cx="48" cy="254" r="45" fill="#1a1d22" role="img" aria-label="Altimeter"/>
        <circle cx="48" cy="355" r="45" fill="#1a1d22" role="img" aria-label="Turn coordinator"/>
        <circle cx="48" cy="458" r="45" fill="#1a1d22" role="img" aria-label="Heading indicator"/>
      </g>
    </svg>

    <p class="front-tagline">
      <span class="gold">PREPARE FOR YOUR IFR</span>
      <span class="white">RATING WITH CONFIDENCE</span>
    </p>
    <div class="rule light" style="left:578px;top:609px;width:389px"></div>
    <p class="front-author">MARCUS J. HOLLOWAY</p>
  </main>
</body>
</html>
```